Body therapist needs a business card

I need a card for my business which is teaching trainings in body therapy, the company is called Wellacombe Educational Group. I teach to massage therapists around Australia, South East Asia and the USA. I am attaching my logo which will guide you as to what colours I would like to have you consider. Please consult my website to find out more about what I do. www.kinetrova.com.au

My name is Gareth Wellacombe. My phone number is (03) 9157 2618 or 0412573086. email is info@kinetrova.com.au

```html
<!DOCTYPE html>
<html lang="en">
<head>
<meta charset="utf-8">
<title>Wellacombe Educational Group – Business Card</title>
<link rel="stylesheet" href="https://fonts.googleapis.com/css2?family=Lato:wght@400;700;900&display=swap">
<style>
  :root {
    --bg: #262626;
    --brown: #5c3323;
    --red: #b01f24;
    --lime: #cddc2c;
    --white: #ffffff;
    --card-w: 620px;
    --card-h: 354px;
  }
  * { box-sizing: border-box; margin: 0; padding: 0; }
  html, body {
    width: 1200px; height: 878px; overflow: hidden;
    background: var(--bg);
    font-family: "Lato", sans-serif;
  }
  .stage { position: relative; width: 1200px; height: 878px; }
  .card {
    position: absolute; left: 290px;
    width: var(--card-w); height: var(--card-h);
    overflow: hidden;
  }
  .card--back { top: 56px; background: var(--brown); }
  .card--front { top: 468px; background: var(--white); }

  /* back */
  .back-mark {
    position: absolute; inset: 0;
    display: flex; align-items: center; justify-content: center; gap: 18px;
  }
  .back-mark__dot { width: 64px; height: 64px; border-radius: 50%; background: var(--lime); }
  .back-mark__name { color: var(--white); font-weight: 900; font-size: 46px; letter-spacing: 0.5px; }

  /* front */
  .edge-tab {
    position: absolute; left: -22px; top: 30px;
    width: 44px; height: 44px; border-radius: 50%; background: var(--brown);
  }
  .person { position: absolute; left: 40px; top: 28px; }
  .person__name { color: var(--brown); font-weight: 900; font-size: 31px; line-height: 1.05; }
  .person__role { color: var(--red); font-size: 18px; margin-top: 2px; }
  .address { position: absolute; left: 40px; top: 122px; color: var(--red); font-size: 17px; line-height: 1.3; }
  .address__company { color: var(--brown); font-weight: 700; }
  .contacts { position: absolute; left: 40px; top: 222px; list-style: none; }
  .contacts__item {
    display: flex; align-items: center; gap: 14px;
    color: var(--red); font-size: 18px; line-height: 1.6;
  }
  .contacts__icon { width: 16px; height: 16px; flex: none; }
  .front-mark {
    position: absolute; right: 34px; top: 150px;
    display: flex; align-items: center; gap: 12px;
  }
  .front-mark__dot { width: 40px; height: 40px; border-radius: 50%; background: var(--lime); }
  .front-mark__name { color: var(--brown); font-weight: 900; font-size: 38px; }
</style>
</head>
<body>
<main class="stage">
  <section class="card card--back" aria-label="Card back">
    <div class="back-mark">
      <span class="back-mark__dot"></span>
      <span class="back-mark__name">Kinetrova</span>
    </div>
  </section>

  <section class="card card--front" aria-label="Card front">
    <span class="edge-tab"></span>
    <header class="person">
      <h1 class="person__name">Gareth Wellacombe</h1>
      <p class="person__role">Founder &amp; Trainer</p>
    </header>
    <address class="address" style="font-style:normal">
      <div class="address__company">Wellacombe Educational Group</div>
      <div>P.O. Box 2847 Ringwood East</div>
      <div>Victoria, 3135 Australia</div>
    </address>
    <ul class="contacts">
      <li class="contacts__item">
        <svg class="contacts__icon" viewBox="0 0 16 16" aria-hidden="true"><path fill="#5c3323" d="M3.6 1.2l2.3 2.6-1.3 1.6c.9 2.2 2.7 4 4.9 4.9l1.6-1.3 2.6 2.3-1.4 2.5C7.2 13.6 2.4 8.8 1.2 2.6z"/></svg>
        <span>(03) 9157 2618</span>
      </li>
      <li class="contacts__item">
        <svg class="contacts__icon" viewBox="0 0 16 16" aria-hidden="true"><rect x="1" y="3.5" width="14" height="9" fill="#5c3323"/><path d="M1.5 4l6.5 5 6.5-5" fill="none" stroke="#fff" stroke-width="1.2"/></svg>
        <span>info@kinetrova.com.au</span>
      </li>
      <li class="contacts__item">
        <svg class="contacts__icon" viewBox="0 0 16 16" aria-hidden="true"><g fill="none" stroke="#5c3323" stroke-width="1.3"><circle cx="8" cy="8" r="6.5"/><ellipse cx="8" cy="8" rx="3" ry="6.5"/><path d="M1.5 8h13M2.6 4.6h10.8M2.6 11.4h10.8"/></g></svg>
        <span>www.kinetrova.com.au</span>
      </li>
    </ul>
    <div class="front-mark">
      <span class="front-mark__dot"></span>
      <span class="front-mark__name">Kinetrova</span>
    </div>
  </section>
</main>
</body>
</html>
```